Youtube Thumbnail templates x 4 for football channel (more than 1 winner will be chosen)

I am looking for a set of 4 thumbnail templates that are on brand.

They should be eye catching and baiting the click.

The 4 different thumbnails will likely be very similar.

It is highly likely that I will choose more than 1 designer as the winner for the project

I have added my brand guidelines below as well as my logo.

The website page to get a good feel for my brand is: https://bravolane.global/474-mentoring/

Also, please feel free to add any images of famous footballers in the template, as these will be delivered in PSD file at the end I will be able to edit these thumbnails before they go live

Football players of all levels

Sans Serif

• Be on brand.
Be eye catching and very clickable

```html
<!DOCTYPE html>
<html lang="en">
<head>
<meta charset="utf-8">
<title>Football Thumbnail Templates</title>
<link href="https://fonts.googleapis.com/css2?family=Montserrat:wght@500;700;800&display=swap" rel="stylesheet">
<style>
  :root{
    --board:#7d7d7d;
    --cyan:#00e6ff;
    --sky:#12c8f4;
    --blue:#1e8ff0;
    --blue-deep:#1d4f9e;
    --outline:#22c4f3;
    --frame:#41b6f5;
    --navy:#1b1e3a;
    --white:#ffffff;
  }
  *{margin:0;padding:0;box-sizing:border-box}
  html,body{width:1200px;height:960px;overflow:hidden;background:var(--board)}
  body{position:relative;font-family:"Montserrat",Arial,sans-serif}
  .thumb{position:absolute;left:207px;width:786px;height:443px;overflow:hidden;box-shadow:0 4px 10px rgba(0,0,0,.35)}
  .thumb--action{top:18px}
  .thumb--promo{top:496px}
  .thumb svg.art{position:absolute;inset:0;width:100%;height:100%}

  .headline{position:absolute;color:var(--white);font-weight:800;text-transform:uppercase;white-space:nowrap;
    -webkit-text-stroke:7px var(--outline);paint-order:stroke fill;
    text-shadow:
      3px 0 0 var(--blue-deep),-3px 0 0 var(--blue-deep),0 3px 0 var(--blue-deep),0 -3px 0 var(--blue-deep),
      3px 3px 0 var(--blue-deep),-3px 3px 0 var(--blue-deep),3px -3px 0 var(--blue-deep),-3px -3px 0 var(--blue-deep),
      5px 6px 10px rgba(0,0,0,.45)}
  .headline--top{left:34px;top:10px;font-size:67px;line-height:.86}
  .headline--side{right:30px;top:166px;font-size:81px;text-align:right;line-height:.85}

  .claim{position:absolute;left:38px;top:178px;color:var(--white);text-transform:uppercase;line-height:57px;white-space:nowrap;
    text-shadow:0 3px 8px rgba(0,0,0,.35)}
  .claim .strong{font-weight:800;font-size:54px;letter-spacing:.5px}
  .claim .soft{font-weight:500;font-size:44px}

  .brand{position:absolute;left:608px;top:310px;width:140px;text-align:center;color:var(--white)}
  .brand-mark{display:block;width:34px;height:34px;margin:0 auto 10px;border-radius:50%;background:var(--white)}
  .brand-name{font-size:7.5px;font-weight:700;letter-spacing:.5px;text-transform:uppercase;white-space:nowrap}
</style>
</head>
<body>

<section class="thumb thumb--action">
  <svg class="art" viewBox="0 0 720 406" preserveAspectRatio="none">
    <defs>
      <linearGradient id="actionPhoto" x1="1" y1="0" x2="0" y2="1">
        <stop offset="0" stop-color="#f6f6f6"/>
        <stop offset=".3" stop-color="#dcdcdc"/>
        <stop offset=".48" stop-color="#6e6e6e"/>
        <stop offset=".6" stop-color="#262626"/>
        <stop offset=".74" stop-color="#3a3a3a"/>
        <stop offset=".88" stop-color="#d2d2d2"/>
        <stop offset="1" stop-color="#f4f4f4"/>
      </linearGradient>
      <linearGradient id="stripeBlue" x1="0" y1="0" x2="0" y2="1">
        <stop offset="0" stop-color="var(--cyan)"/>
        <stop offset="1" stop-color="var(--blue)"/>
      </linearGradient>
    </defs>
    <rect class="photo" role="img" aria-label="Black and white photo of a footballer striking an overhead kick" width="720" height="406" fill="url(#actionPhoto)"/>
    <polygon points="585,0 690,0 600,406 490,406" fill="url(#stripeBlue)"/>
    <polygon points="695,0 716,0 664,170 643,170" fill="var(--white)"/>
    <polygon points="720,20 720,60 686,170 674,150" fill="var(--white)"/>
    <polygon points="720,90 720,406 640,406" fill="var(--blue)" opacity=".9"/>
  </svg>
  <h2 class="headline headline--top">Use your<br>brain</h2>
  <h2 class="headline headline--side">Raise<br>your<br>game</h2>
</section>

<section class="thumb thumb--promo">
  <svg class="art" viewBox="0 0 720 404" preserveAspectRatio="none">
    <defs>
      <linearGradient id="promoBg" x1="0" y1="0" x2="1" y2="1">
        <stop offset="0" stop-color="var(--cyan)"/>
        <stop offset=".45" stop-color="var(--sky)"/>
        <stop offset="1" stop-color="var(--navy)"/>
      </linearGradient>
      <linearGradient id="promoShade" x1="0" y1="0" x2="1" y2="1">
        <stop offset="0" stop-color="var(--blue)"/>
        <stop offset="1" stop-color="var(--navy)"/>
      </linearGradient>
      <linearGradient id="playerPhoto" x1="0" y1="0" x2="0" y2="1">
        <stop offset="0" stop-color="#3a3a44"/>
        <stop offset=".5" stop-color="#a8262c"/>
        <stop offset=".75" stop-color="#8a2a2e"/>
        <stop offset="1" stop-color="#3f8a3a"/>
      </linearGradient>
      <clipPath id="photoCut"><polygon points="530,-14 680,136 530,286 380,136"/></clipPath>
    </defs>
    <rect width="720" height="404" fill="url(#promoBg)"/>
    <polygon points="0,404 410,0 720,0 720,404" fill="url(#promoShade)" opacity=".75"/>
    <polygon points="152,21 219,88 152,155 85,88" fill="url(#promoShade)"/>
    <polygon points="530,-46 712,136 530,318 348,136" fill="none" stroke="var(--frame)" stroke-width="24"/>
    <g clip-path="url(#photoCut)">
      <rect class="photo" role="img" aria-label="Photo of a footballer in a red and white kit running on the pitch" x="380" y="-14" width="300" height="300" fill="url(#playerPhoto)"/>
    </g>
  </svg>
  <p class="claim">
    <span class="strong">The best</span><br>
    <span class="strong">Players</span> <span class="soft">are</span><br>
    <span class="soft">Consistently on</span><br>
    <span class="strong">Top form</span>
  </p>
  <div class="brand">
    <span class="brand-mark"></span>
    <span class="brand-name">Alan Mercer Hypnotherapy</span>
  </div>
</section>

</body>
</html>
```